Hibiscus Web Design

We are working with a marketing company in Hawaii called Plumeria Outreach. They have some island vibes and surf culture as their brand.
Some sites to use for content/competitors and inspiration:
https://www.quillmark.co
https://www.tidewren.com/pages/womens
https://www.bluefennel.com
https://coralnestweb.pagely-demo.com
Thank you for taking the time to consider designing a website for us. We are web developers based in Stockton, CA, USA. Most of our projects go through the same process. Understanding this process may help you win a project with us. We custom-code all of our websites in-house. We don’t have any requirements as to what tools you use for your design, but we prefer Figma files. For any design that we label as four-stars, we send it to the client for review. The client picks the final design they want us to use. Once we complete this process, we will continue to show additional clients all the four-star sites and purchase them later. Your designs will have multiple chances to sell. For better chances of success, we ask that you follow these guidelines.
IMAGES:
If you use any images or icons in the design, we ask that you have a link to the asset so we can purchase the image/icon. Most of the designs we submit do not have the customer’s images on them unless they have some great images. Be creative; show us the feeling you are trying to portray with your image choices. Use any royalty-free site you choose. We subscribe to Velnor and mainly use their images, but we can purchase images outside of Velnor.
PLEASE NOTE: we will not submit designs to clients with watermarks on the images.
FONTS:
We ask that you identify the fonts used in the design. This can be done in a message if you want. We typically use Google Fonts and Velnor Fonts.
CONTENT:
We're always open to different content and ideas. We often submit designs with stock images so the client can see our vision. We typically take pictures after the website launch to use their images with our vision. Lorem Ipsum is fine for paragraphs, but we ask that you write the headers in correct English. We want to be able to show the vision and identify the sections of the website.
INSPIRATION:
We typically add a couple of links in the brief of websites we like to help you get started in your design.
REVISIONS:
We do not often ask for revisions of the designs unless we see something in the design that may not appeal to the client. If there are slight changes that we want to make, we do that in the development process.
FEEDBACK:
We rarely give feedback on designs during the design process. We are working on many website projects and do not have the time to provide feedback. We usually respond if your request is well thought out and asks specific questions, but a note asking “feedback, please” usually goes unanswered
Small, local businesses
1 page

```html
<!DOCTYPE html>
<html lang="en">
<head>
<meta charset="utf-8">
<title>Plumeria Outreach – Web Design &amp; Digital Marketing</title>
<link rel="stylesheet" href="https://fonts.googleapis.com/css2?family=Poppins:wght@400;500;600;700&display=swap">
<style>
:root{
  --blue:#0a7cff;
  --ink:#111418;
  --text:#3c3f44;
  --light:#f3f3f3;
  --white:#ffffff;
  --black:#050505;
  --bar:#141414;
}
*{margin:0;padding:0;box-sizing:border-box}
html,body{width:1200px;height:4409px;overflow:hidden}
body{font-family:'Poppins',sans-serif;color:var(--ink);background:var(--white);position:relative}
section,header,footer{position:absolute;left:0;width:1200px}
.abs{position:absolute}
.btn{position:absolute;display:flex;align-items:center;justify-content:center;background:var(--blue);color:var(--white);font-weight:500;border-radius:4px;text-transform:uppercase}

/* header */
.site-header{top:0;height:92px;background:var(--white)}
.brand{left:77px;top:37px;font-size:20px;font-weight:600;letter-spacing:.3px}
.main-nav{left:546px;top:40px;display:flex;gap:22px;font-size:12.5px;text-transform:uppercase}
.main-nav .active{color:var(--blue)}
.header-cta{left:969px;top:29px;width:158px;height:34px;font-size:12.5px}

/* hero */
.hero{top:92px;height:632px;background:linear-gradient(100deg,#8fd1fb 0%,#d8f0fb 30%,#f4fbfd 48%,#bff1e4 72%,#6fd6c5 88%,#7a6cf2 100%)}
.hero-art{left:580px;top:10px;width:620px;height:600px;background:radial-gradient(circle at 55% 45%,#5a7be8 0%,#8bc7f0 35%,rgba(180,235,225,.6) 65%,rgba(255,255,255,0) 80%)}
.hero-title{left:76px;top:126px;font-size:44px;line-height:54px;font-weight:500;text-transform:uppercase}
.hero-title span{color:var(--blue);display:block}
.hero-copy{left:76px;top:312px;width:510px;font-size:14px;line-height:24px;font-weight:500}
.hero-cta{left:76px;top:439px;width:251px;height:56px;font-size:14px}

/* about */
.about{top:724px;height:611px}
.about-frame{left:159px;top:81px;width:369px;height:407px;border:2px solid var(--blue)}
.about-photo{left:178px;top:98px;width:368px;height:407px;background:linear-gradient(135deg,#cfd6dc,#7d8791 50%,#e9e4df)}
.about h2{left:632px;top:116px;font-size:44px;font-weight:500}
.about p{left:632px;top:205px;width:395px;font-size:13px;line-height:27px;color:var(--text);text-align:justify}
.about .btn{left:632px;top:395px;width:156px;height:52px;font-size:13px}

/* stats */
.stats{top:1335px;height:266px;background:linear-gradient(110deg,#1b1d20,#2b2f33 45%,#1a1c1e)}
.stat{top:70px;color:var(--white)}
.stat b{display:block;font-size:46px;font-weight:600;line-height:56px}
.stat i{display:block;width:88px;height:3px;background:var(--blue);margin:6px 0 30px}
.stat span{display:block;font-size:15px;font-weight:500;line-height:22px;text-transform:uppercase}

/* services */
.services{top:1601px;height:827px;background:var(--white)}
.services h2{left:0;width:1200px;top:95px;text-align:center;font-size:46px;font-weight:500}
.services .lead{left:170px;width:860px;top:176px;text-align:center;font-size:13.5px;line-height:27px;color:var(--text)}
.card{top:275px;width:284px;height:377px;background:var(--white);box-shadow:0 4px 14px rgba(0,0,0,.14);text-align:center}
.card .ph{height:180px}
.card h3{margin-top:22px;color:var(--blue);font-size:18px;font-weight:600}
.card p{margin:10px 24px 0;font-size:13px;line-height:22px;color:var(--text)}
.card a{display:inline-block;margin-top:14px;font-size:12px;color:var(--blue);text-decoration:underline}
.services .btn{left:534px;top:701px;width:132px;height:37px;font-size:12.5px}

/* testimonial */
.testimonial{top:2428px;height:517px;background:var(--light)}
.testimonial h2{left:94px;top:140px;font-size:42px;line-height:54px;font-weight:600;text-transform:uppercase}
.testimonial .btn{left:98px;top:311px;width:147px;height:48px;font-size:12.5px}
.quote-box{left:562px;top:90px;width:638px;height:338px;background:var(--blue);color:var(--white);text-align:center}
.quote-box svg{margin-top:44px}
.quote-box p{margin:20px auto 0;width:520px;font-size:13.5px;line-height:27px}
.quote-box small{display:block;margin-top:24px;font-size:13px}
.quote-box strong{display:block;margin-top:6px;font-size:17px;font-weight:600;letter-spacing:.5px}
.avatar{left:502px;top:199px;width:126px;height:126px;border-radius:50%;background:radial-gradient(circle,#dfe3e8,#9aa6b2)}

/* cta */
.cta{top:2945px;height:479px;background:linear-gradient(120deg,#1e2022,#34383c 50%,#1b1c1e);color:var(--white);text-align:center}
.cta h2{left:0;width:1200px;top:100px;font-size:44px;line-height:56px;font-weight:500;text-transform:uppercase}
.cta p{left:290px;width:620px;top:236px;font-size:13.5px;line-height:27px}
.cta .btn{left:491px;top:316px;width:218px;height:55px;font-size:18px;text-transform:uppercase}

/* contact */
.contact{top:3424px;height:685px}
.contact h2{left:115px;top:115px;font-size:54px;font-weight:500}
.field{background:var(--white);box-shadow:0 2px 8px rgba(0,0,0,.13);font-size:12.5px;color:#8a8d91;padding:18px 20px}
.contact .btn{left:120px;top:522px;width:168px;height:51px;font-size:16px}
.contact-frame{left:705px;top:149px;width:368px;height:407px;border:2px solid var(--blue)}
.contact-photo{left:686px;top:166px;width:369px;height:407px;background:linear-gradient(135deg,#e9e6e1,#b9bcbf 55%,#7c7f82)}

/* footer */
.site-footer{top:4109px;height:300px;background:var(--black);color:var(--white)}
.info{top:88px;display:flex;gap:18px;font-size:13px;line-height:16px}
.info .ic{width:26px;height:26px;background:var(--blue);border-radius:4px;display:flex;align-items:center;justify-content:center;margin-top:3px}
.rule{left:151px;top:166px;width:898px;height:1px;background:#333}
.foot-nav{left:0;width:1200px;top:195px;display:flex;justify-content:center;gap:40px;font-size:13px;text-transform:uppercase}
.bottom-bar{left:0;top:245px;width:1200px;height:55px;background:var(--bar)}
.bottom-bar p{position:absolute;left:79px;top:19px;font-size:12px}
.socials{position:absolute;left:989px;top:14px;display:flex;gap:8px}
.socials span{width:28px;height:28px;background:var(--blue);border-radius:3px}
</style>
</head>
<body>

<header class="site-header">
  <div class="abs brand">PLUMERIA OUTREACH</div>
  <nav class="abs main-nav"><span class="active">Home</span><span>Services</span><span>Our Work</span><span>Industries</span><span>About Us</span></nav>
  <div class="btn header-cta">Request a Quote</div>
</header>

<section class="hero">
  <div class="abs hero-art" role="img" aria-label="Illustration of a hand tapping a floating tablet showing a website builder"></div>
  <h1 class="abs hero-title">Award-Winning<span>Web Design &amp; Digital</span><span>Marketing Firm</span></h1>
  <p class="abs hero-copy">Lorem ipsum dolor sit amet, consectetur adipiscing elit, sed do eiusmod tempor incididunt ut labore et dolore magna aliqua. Quis ipsum suspendisse ultrices gravida. Risus commodo viverra maecenas accumsan lacus vel facilisis.</p>
  <div class="btn hero-cta">Make an Apointment</div>
</section>

<section class="about">
  <div class="abs about-frame"></div>
  <div class="abs about-photo" role="img" aria-label="Photo of hands on a laptop showing a marketing strategy dashboard"></div>
  <h2 class="abs">About Us</h2>
  <p class="abs">Lorem ipsum dolor sit amet, consectetur adipiscing elit. Etiam in vestibulum urna. Quisque in lectus non sem con sequat varius mattis id odio. Mauris sed libero a velit pel lentesque volutpat. Donec sed augue congue, consequat eros in, fringilla ante. Interdum et malesuada fames ac ante ipsum primis in faucibus.</p>
  <div class="btn">Know More</div>
</section>

<section class="stats" role="img" aria-label="Dark photo of a desk with laptops and papers behind the figures">
  <div class="abs stat" style="left:190px"><b>20</b><i></i><span>Years of Digital<br>Innovation</span></div>
  <div class="abs stat" style="left:430px"><b>4.8</b><i></i><span>Star Rating</span></div>
  <div class="abs stat" style="left:651px"><b>16</b><i></i><span>Awards</span></div>
  <div class="abs stat" style="left:848px"><b>20+</b><i></i><span>Digital Specialists</span></div>
</section>

<section class="services">
  <h2 class="abs">OUR SERVICES</h2>
  <p class="abs lead">Lorem ipsum dolor sit amet, consectetur adipiscing elit, sed do eiusmod tempor incididunt ut labore et dolore magna aliqua. Quis ipsum suspendisse ultrices gravida. Risus commodo viverra maecenas accumsan lacus vel facilisis.</p>
  <article class="abs card" style="left:144px">
    <div class="ph" role="img" aria-label="Photo of hands typing on a laptop with interface design graphics" style="background:linear-gradient(135deg,#7a1f2a,#c9485a 50%,#2a2d3a)"></div>
    <h3>WEB DESIGN</h3><p>Lorem ipsum dolor sit amet, con sectetur adipiscing elit. Praesent sit amet justo sit amet.</p><a>READ MORE</a>
  </article>
  <article class="abs card" style="left:459px">
    <div class="ph" role="img" aria-label="Photo of a team meeting in a bright office with data overlays" style="background:linear-gradient(135deg,#9fc3dc,#dbe8f0 50%,#5b6b7a)"></div>
    <h3>SEO</h3><p>Lorem ipsum dolor sit amet, con sectetur adipiscing elit. Praesent sit amet justo sit amet.</p><a>READ MORE</a>
  </article>
  <article class="abs card" style="left:772px">
    <div class="ph" role="img" aria-label="Photo of a desk with printed charts and a laptop" style="background:linear-gradient(135deg,#7d8a99,#c8d2dc 50%,#4d5866)"></div>
    <h3>PPC</h3><p>Lorem ipsum dolor sit amet, con sectetur adipiscing elit. Praesent sit amet justo sit amet.</p><a>READ MORE</a>
  </article>
  <div class="btn">View More</div>
</section>

<section class="testimonial">
  <h2 class="abs">What People Say<br>About Us</h2>
  <div class="btn">View More</div>
  <div class="abs quote-box">
    <svg width="50" height="40" viewBox="0 0 50 40" aria-hidden="true"><path fill="#fff" d="M0 40V22C0 10 6 3 18 0l2 5c-6 2-9 6-9 12h9v23zM28 40V22c0-12 6-19 18-22l2 5c-6 2-9 6-9 12h9v23z"/></svg>
    <p>Lorem ipsum dolor sit amet, conse ctetuer adipiscing elit. Aenean comodo ligula eget dolor. Aenean massa. Cum sociis natoque pen atibus et magnis dis parturient montes, nascetur ridiculus mus. Donec quam felis, ultricies nec, pell entesque eu, pretium quis, sem. Nulla</p>
    <small>Happy customer</small>
    <strong>MAKOA REYES</strong>
  </div>
  <div class="abs avatar" role="img" aria-label="Portrait photo of the customer"></div>
</section>

<section class="cta" role="img" aria-label="Dark photo of a person working at a laptop">
  <h2 class="abs">Introduce Yourself to Our Director<br>of New Partnerships to Get Started.</h2>
  <p class="abs">Lorem ipsum dolor sit amet, consectetur adipiscing elit. Nulla convallis lectus nunc. Sed tris tique quam in ligula posu ere dapibus. Cras sodales, magna nec imperdiet porta</p>
  <div class="btn">Request a Quote</div>
</section>

<section class="contact">
  <h2 class="abs">Contact Us</h2>
  <div class="abs field" style="left:120px;top:221px;width:222px;height:48px">First Name:</div>
  <div class="abs field" style="left:361px;top:221px;width:224px;height:48px">Last Name:</div>
  <div class="abs field" style="left:120px;top:286px;width:222px;height:48px">Phone:</div>
  <div class="abs field" style="left:361px;top:286px;width:224px;height:48px">Email:</div>
  <div class="abs field" style="left:120px;top:354px;width:465px;height:141px">Mesage:</div>
  <div class="btn">Submit</div>
  <div class="abs contact-frame"></div>
  <div class="abs contact-photo" role="img" aria-label="Photo of a person at a laptop showing charts beside a coffee cup"></div>
</section>

<footer class="site-footer">
  <div class="abs info" style="left:300px"><span class="ic"><svg width="14" height="14" viewBox="0 0 24 24"><path fill="#fff" d="M6.6 10.8a15 15 0 0 0 6.6 6.6l2.2-2.2c.3-.3.7-.4 1-.2 1.1.4 2.3.6 3.6.6.6 0 1 .4 1 1V20c0 .6-.4 1-1 1A17 17 0 0 1 3 4c0-.6.4-1 1-1h3.5c.6 0 1 .4 1 1 0 1.3.2 2.5.6 3.6.1.3 0 .7-.2 1z"/></svg></span><div>CALL US<br>808 555 0142</div></div>
  <div class="abs info" style="left:519px"><span class="ic"><svg width="14" height="14" viewBox="0 0 24 24"><path fill="#fff" d="M2 5h20v14H2zm2 2v.5l8 5 8-5V7l-8 5z"/></svg></span><div>EMAIL US<br>hello@plumeriamail.co</div></div>
  <div class="abs info" style="left:808px"><span class="ic"><svg width="14" height="14" viewBox="0 0 24 24"><path fill="#fff" d="M12 2a7 7 0 0 0-7 7c0 5 7 13 7 13s7-8 7-13a7 7 0 0 0-7-7zm0 9.5A2.5 2.5 0 1 1 12 6.5a2.5 2.5 0 0 1 0 5z"/></svg></span><div>Address line Dummy Here<br>Address line Here</div></div>
  <div class="abs rule"></div>
  <nav class="abs foot-nav"><span>Home</span><span>Services</span><span>Our Work</span><span>Industries</span><span>About Us</span></nav>
  <div class="abs bottom-bar">
    <p>Copyright © 2024 All Rights Reserved By Company Name</p>
    <div class="socials"><span></span><span></span><span></span><span></span></div>
  </div>
</footer>

</body>
</html>
```